Design a Banner for wood website

Need a 1345px by 400px banner (layered photoshop file w/png) created for a company that sells ipe wood decking.
- Must show ipe wood images within the design
- Must have text stating "Get a Quote!"

```html
<!DOCTYPE html>
<html lang="en">
<head>
<meta charset="UTF-8">
<title>Ipe Wood Decking – Get a Quote</title>
<link rel="stylesheet" href="https://fonts.googleapis.com/css2?family=Josefin+Sans:wght@300&family=Cinzel:wght@600&display=swap">
<style>
  :root {
    --wood-deep: #2a0f06;
    --wood-dark: #5a210d;
    --wood-mid: #8a3a16;
    --wood-warm: #b8602a;
    --glow-amber: #d9904f;
    --glow-light: #f2c99a;
    --base-shadow: #140804;
    --title-cream: #f1dcbc;
    --cta-brown: #3b1a0b;
  }
  html, body {
    margin: 0;
    padding: 0;
    overflow: hidden;
    background: var(--base-shadow);
  }
  .banner {
    position: relative;
    width: 1200px;
    height: 402px;
    overflow: hidden;
  }
  .wood-photo {
    position: absolute;
    inset: 0;
    background:
      radial-gradient(ellipse 170px 55px at 700px 210px, rgba(242, 201, 154, 0.85), rgba(242, 201, 154, 0) 100%),
      linear-gradient(90deg, rgba(20, 8, 4, 0.55) 0%, rgba(20, 8, 4, 0) 18%, rgba(20, 8, 4, 0) 82%, rgba(20, 8, 4, 0.5) 100%),
      linear-gradient(180deg,
        var(--wood-dark) 0%,
        var(--wood-mid) 30%,
        var(--wood-warm) 42%,
        var(--glow-amber) 52%,
        var(--glow-amber) 62%,
        var(--wood-mid) 74%,
        var(--wood-deep) 84%,
        var(--base-shadow) 100%);
  }
  .headline {
    position: absolute;
    top: 62px;
    left: 0;
    width: 100%;
    margin: 0;
    text-align: center;
    font-family: "Josefin Sans", sans-serif;
    font-weight: 300;
    font-size: 58px;
    letter-spacing: 0.3em;
    text-indent: 0.3em;
    color: var(--title-cream);
    line-height: 1;
  }
  .cta {
    position: absolute;
    top: 240px;
    left: 0;
    width: 100%;
    margin: 0;
    text-align: center;
    font-family: "Cinzel", serif;
    font-weight: 600;
    font-size: 32px;
    letter-spacing: 0.06em;
    color: var(--cta-brown);
    line-height: 1;
  }
</style>
</head>
<body>
  <div class="banner">
    <div class="wood-photo" role="img" aria-label="Close-up photograph of polished ipe wood decking boards with warm reddish-brown grain"></div>
    <h1 class="headline">IPE WOOD DECKING</h1>
    <p class="cta">-GET A QUOTE-</p>
  </div>
</body>
</html>
```